Need help in designing new business card utilizing our new logo.

BuildMarq Solutions works with Construction Business Owners, Managers & IT Professionals to strengthen software usage and increase user productivity.

Our Construction Accounting and Mobile Field Management Software Clients engage with us in the following areas:

New Software Implementations
Software Re-Implementations
Redesigning Software Usage at the User Level
Project Coordination & Management
Continued Software Support

Old tag line:
Weighing Options - Implementing Solutions

www.buildmarq-solutions.example

Stride 4 is a product, but not needed for a new business card.

```html
<!DOCTYPE html>
<html lang="en">
<head>
<meta charset="utf-8">
<title>BuildMarq Solutions – Business Card</title>
<link href="https://fonts.googleapis.com/css2?family=Arimo:wght@400;700&display=swap" rel="stylesheet">
<style>
  :root {
    --brand-blue: #2222a8;
    --brand-grey: #9e9e9e;
    --text-grey: #6f6f6f;
    --card-white: #ffffff;
    --card-dark: #2a2a2a;
    --backdrop: #e4e2e2;
  }
  * { margin: 0; padding: 0; box-sizing: border-box; }
  html, body { width: 1200px; height: 675px; overflow: hidden; }
  body {
    background: var(--backdrop);
    font-family: "Arimo", Arial, sans-serif;
    position: relative;
  }
  .card {
    position: absolute;
    top: 200px;
    width: 480px;
    height: 274px;
    overflow: hidden;
    box-shadow: 0 6px 18px rgba(0,0,0,0.18);
  }
  .card--front { left: 90px; background: var(--card-white); }
  .card--back { left: 630px; background: var(--card-dark); }

  .accent-band { position: absolute; top: 0; bottom: 0; }
  .card--front .accent-band--blue { right: 56px; width: 22px; background: var(--brand-blue); }
  .card--front .accent-band--grey { right: 0; width: 44px; background: var(--brand-grey); }
  .card--back .accent-band--blue { right: 98px; width: 22px; background: var(--brand-blue); }
  .card--back .accent-band--grey { width: 22px; background: var(--brand-grey); }
  .card--back .accent-band--grey.one { right: 62px; }
  .card--back .accent-band--grey.two { right: 26px; }

  .brand { position: absolute; display: flex; align-items: center; gap: 10px; }
  .brand-mark { width: 16px; height: 16px; background: var(--brand-blue); }
  .brand-name { font-weight: 700; color: var(--brand-blue); letter-spacing: 0.5px; }
  .card--front .brand { left: 34px; top: 34px; }
  .card--front .brand-name { font-size: 22px; }

  .holder { position: absolute; left: 34px; top: 110px; }
  .holder-name { font-size: 17px; font-weight: 700; color: var(--brand-blue); }
  .holder-title { font-size: 12px; color: var(--text-grey); margin-top: 2px; }

  .contact { position: absolute; left: 34px; top: 165px; list-style: none; }
  .contact li {
    display: flex; align-items: center; gap: 8px;
    font-size: 12px; color: var(--text-grey); margin-bottom: 6px;
  }
  .contact svg { width: 16px; height: 16px; flex: none; }
  .address { position: absolute; left: 34px; top: 222px; font-size: 12px; line-height: 1.4; color: var(--text-grey); }

  .card--back .brand { left: 34px; top: 100px; }
  .card--back .brand-name { font-size: 26px; }
  .website { position: absolute; left: 34px; top: 148px; font-size: 13px; font-weight: 700; color: #ffffff; letter-spacing: 0.5px; }
</style>
</head>
<body>
  <section class="card card--front" aria-label="Card front">
    <div class="accent-band accent-band--blue"></div>
    <div class="accent-band accent-band--grey"></div>
    <div class="brand">
      <span class="brand-mark"></span>
      <span class="brand-name">BuildMarq Solutions</span>
    </div>
    <div class="holder">
      <p class="holder-name">Dana R. Whitfield</p>
      <p class="holder-title">Owner</p>
    </div>
    <ul class="contact">
      <li>
        <svg viewBox="0 0 16 16" aria-hidden="true"><circle cx="8" cy="8" r="8" fill="var(--brand-blue)"/><path d="M5.4 4.2l1.4 1.6-.7 1a5 5 0 0 0 2.1 2.1l1-.7 1.6 1.4-.8 1.2C7.6 10.7 5.3 8.4 4.2 6.2z" fill="#fff"/></svg>
        555-014-2290
      </li>
      <li>
        <svg viewBox="0 0 16 16" aria-hidden="true"><circle cx="8" cy="8" r="8" fill="var(--brand-blue)"/><rect x="4" y="5.2" width="8" height="5.6" fill="none" stroke="#fff" stroke-width="1"/><path d="M4 5.4l4 3 4-3" fill="none" stroke="#fff" stroke-width="1"/></svg>
        dwhitfield@buildmarq-solutions.example
      </li>
    </ul>
    <p class="address">48 Alder Lane - Suite 12<br>Lakeford NY 10000</p>
  </section>

  <section class="card card--back" aria-label="Card back">
    <div class="accent-band accent-band--blue"></div>
    <div class="accent-band accent-band--grey one"></div>
    <div class="accent-band accent-band--grey two"></div>
    <div class="brand">
      <span class="brand-mark"></span>
      <span class="brand-name">BuildMarq Solutions</span>
    </div>
    <p class="website">www.buildmarq-solutions.example</p>
  </section>
</body>
</html>
```